Redesign website for Wine Warehouse and Logistics company

We are looking to redesign https://www.brindlefreight.com/ website.

19 minute video showing what needs to be done:
https://files.quorvex.com/file/d/7kQ2mZ9xTbLw4RcVn8HsYpJd3FgA1eU/view?usp=sharing

Quorvex Deck shown in the video:
https://slides.quorvex.com/presentation/d/4pXr8wLmTq2ZbVn7KcJh3FsDyGe9RuAo5NiWtMkPzQa/edit?usp=sharing

I am also offering a $100 bonus on top of the contest award.
Updates

Holidays in India so we did not get enough design entries or quality.

Industry/Entity Type

Logistics company that handles Wine for Wineries.

Number of Pages Required

3 page

Colors

Designer to choose colors to be used in the design.

Requirements
Must have
• Check the 19 minute video showing what needs to be done.

```html
<!DOCTYPE html>
<html lang="en">
<head>
<meta charset="utf-8">
<title>Brindle Freight — Fulfillment built for Wineries</title>
<link rel="stylesheet" href="https://fonts.googleapis.com/css2?family=Open+Sans:wght@400;600;700&family=Noto+Sans:wght@400;500;600&display=swap">
<style>
:root{
  --navy:#0f3a52;
  --navy-dark:#0b2a3c;
  --ink:#1c2a35;
  --muted:#6b7780;
  --line:#d5dbe0;
  --bg:#f4f5f6;
  --page:#ffffff;
  --footer:#dfe5ea;
  --soft:#eef0f2;
  --red:#c8202a;
}
*{box-sizing:border-box;margin:0;padding:0}
html,body{width:1200px;height:3574px;overflow:hidden}
body{background:var(--bg);font-family:"Open Sans",sans-serif;color:var(--ink)}
.page{position:absolute;left:150px;top:97px;width:913px;height:3389px;background:var(--page);overflow:hidden}
.abs{position:absolute}
.heading{font-family:"Noto Sans",sans-serif;font-weight:500;color:var(--ink)}
.btn{position:absolute;display:flex;align-items:center;justify-content:center;border-radius:20px;font-size:10px;font-weight:600}
.btn-solid{background:var(--navy);color:#fff}
.btn-line{border:1px solid var(--line);color:var(--navy);background:#fff}
/* nav */
.logo{display:flex;align-items:center;gap:5px;font-family:"Noto Sans",sans-serif;font-weight:600;font-size:13px;color:var(--navy);letter-spacing:.5px}
.logo-mark{width:14px;height:14px;background:var(--navy);border-radius:50%}
.nav-links{left:286px;top:14px;display:flex;gap:17px;font-size:10.5px;color:var(--navy)}
.nav-links .active{border-bottom:1px solid var(--navy);padding-bottom:2px}
/* hero */
.hero-art{left:65px;top:67px;width:313px;height:378px;border-radius:40% 40% 30% 30%;background:radial-gradient(circle at 45% 40%,#d99a5e 0%,#f1c6b3 55%,#fff 72%)}
.hero-title{left:420px;top:158px;width:342px;text-align:center;font-size:23px;color:var(--navy)}
.hero-sub{left:450px;top:210px;width:282px;text-align:center;font-size:10px;line-height:16px;color:var(--navy)}
/* stats */
.aio{position:absolute;left:68px;top:565px;width:140px;font-family:"Noto Sans",sans-serif;color:#111;line-height:1}
.stat{position:absolute;font-size:8px;color:var(--muted);text-align:center;line-height:12px}
.stat b{display:block;font-family:"Noto Sans",sans-serif;font-weight:600;font-size:22px;color:#111;line-height:30px}
.stat span{color:#111}
.svc{position:absolute;width:110px;height:36px;background:#fff;box-shadow:0 2px 6px rgba(0,0,0,.12);font-size:8px;text-align:center;display:flex;align-items:center;justify-content:center;line-height:11px;color:#333}
.svc-icon{position:absolute;width:62px;height:62px;border-radius:50%;background:#fff;box-shadow:0 2px 8px rgba(0,0,0,.12);display:flex;align-items:center;justify-content:center}
/* why */
.eyebrow{font-size:9px;color:var(--muted)}
.why-title{left:68px;top:1102px;width:420px;font-size:25px;line-height:32px}
.barrels{left:193px;top:1216px;width:255px;height:262px;background:radial-gradient(ellipse at 50% 40%,#4a3a2c 0%,#1d1712 60%,#0b0907 100%)}
.ticks{list-style:none;font-size:8.5px;color:#333}
.ticks li{display:flex;align-items:center;gap:8px;height:19px}
.ticks li::before{content:"";width:9px;height:9px;border-radius:50%;background:var(--navy);flex:none}
/* software band */
.band{left:0;top:1564px;width:913px;height:281px;background:linear-gradient(90deg,#0a2230,#163a4e 60%,#0e2a3a)}
.tabs{left:68px;top:44px;display:flex;border:1px solid rgba(255,255,255,.4)}
.tabs div{width:112px;height:39px;font-size:8.5px;color:#fff;display:flex;align-items:center;justify-content:center;border-right:1px solid rgba(255,255,255,.4);text-align:center;line-height:11px}
.tabs .lead{justify-content:flex-start;padding-left:10px;text-align:left;background:rgba(0,0,0,.25)}
.tabs .on{background:#fff;color:var(--navy)}
.laptop{left:582px;top:86px;width:262px;height:195px}
/* warehouse */
.wh-title{left:68px;top:1952px;font-size:13px;color:var(--ink);font-weight:400}
.wh-title b{color:var(--navy);font-weight:600}
.para{font-size:9px;line-height:17px;color:#333}
.map{left:385px;top:1953px;width:459px;height:296px;background:radial-gradient(ellipse at 50% 50%,#f1f1f1 0%,#fff 75%);border-radius:20px}
/* ship */
.ship{left:0;top:2356px;width:913px;height:392px;background:var(--navy)}
.truck{left:605px;top:2454px;width:235px;height:335px;border-radius:8px;background:linear-gradient(180deg,#e9ecef,#b9bec4 60%,#8d939a);z-index:2}
/* testimonial */
.testi{left:0;top:2748px;width:913px;height:391px;background:var(--soft);z-index:1}
.testi-left{left:0;top:0;width:316px;height:391px;background:#fff}
.client{left:128px;top:57px;width:250px;height:267px;background:#fff;box-shadow:0 2px 10px rgba(0,0,0,.12);display:flex;align-items:center;justify-content:center;font-family:"Noto Sans",sans-serif;font-size:30px;color:var(--red);font-weight:500;text-align:center;line-height:38px}
.quote{left:473px;top:104px;width:380px;font-family:"Noto Sans",sans-serif;font-size:18.5px;line-height:21.5px;color:var(--navy)}
.arrow-btn{position:absolute;width:24px;height:24px;border-radius:50%;border:1px solid #aab}
/* footer */
.footer{left:0;top:3139px;width:913px;height:209px;background:var(--footer);font-size:8.5px;color:#333}
.foot-links{position:absolute;right:355px;top:42px;text-align:right;line-height:25px;font-size:8.5px}
.bottom{left:0;top:3348px;width:913px;height:41px;background:var(--navy-dark);color:#fff;font-size:9px;display:flex;align-items:center;padding-left:68px}
</style>
</head>
<body>
<div class="page">

  <!-- navigation -->
  <div class="abs logo" style="left:68px;top:15px"><span class="logo-mark"></span>BRINDLE FREIGHT</div>
  <nav class="abs nav-links"><span class="active">Wine Fulfillment</span><span>Wine Compliance</span><span>Why Brindle</span><span>Integration</span></nav>
  <svg class="abs" style="left:688px;top:17px" width="12" height="12" viewBox="0 0 12 12"><circle cx="5" cy="5" r="4" fill="none" stroke="#0f3a52" stroke-width="1.3"/><line x1="8" y1="8" x2="11" y2="11" stroke="#0f3a52" stroke-width="1.3"/></svg>
  <span class="abs" style="left:716px;top:15px;font-size:10.5px;color:var(--navy)">Sign In</span>
  <div class="btn btn-solid" style="left:763px;top:10px;width:77px;height:25px">Sign Up</div>

  <!-- hero -->
  <div class="abs hero-art" role="img" aria-label="Line illustration of a woman with bob hair and vines across her shoulder"></div>
  <h1 class="abs heading hero-title">Fulfillment built for Wineries!</h1>
  <svg class="abs" style="left:685px;top:186px" width="80" height="10"><path d="M2 8 Q40 0 78 4" fill="none" stroke="#0f3a52" stroke-width="1.2"/></svg>
  <p class="abs hero-sub">Tech-enabled 3PL that fulfills tasting room and<br>e-Commerce orders for direct-to-consumer<br>wine fulfillment</p>
  <div class="btn btn-solid" style="left:477px;top:284px;width:103px;height:31px">Learn More</div>
  <div class="btn btn-line" style="left:591px;top:284px;width:111px;height:31px;gap:6px">
    <svg width="11" height="11" viewBox="0 0 24 24"><path d="M6 2l4 4-2 3c1 3 4 6 7 7l3-2 4 4-3 4C10 21 3 14 2 5z" fill="none" stroke="#0f3a52" stroke-width="2"/></svg>(000) 000-0000</div>
  <svg class="abs" style="left:571px;top:341px" width="40" height="40"><circle cx="20" cy="20" r="19" fill="#0f3a52" opacity=".25"/><circle cx="20" cy="20" r="15" fill="#0f3a52"/><path d="M16 13 L27 20 L16 27 Z" fill="none" stroke="#fff" stroke-width="1.5"/></svg>

  <!-- all in one -->
  <div class="aio">
    <div style="font-size:25px;margin-left:88px">ALL</div>
    <div style="display:flex;align-items:center;margin-left:35px"><span style="width:22px;height:22px;border:1px solid #111;border-radius:50%;font-size:9px;display:flex;align-items:center;justify-content:center">IN</span><span style="font-size:40px;font-weight:500;margin-left:-4px">ONE</span></div>
    <div style="font-size:25px">SOLUTION</div>
  </div>
  <div class="stat" style="left:68px;top:708px;width:85px"><b>99.95%</b><span>Accuracy rate</span><br>in fulfilling orders</div>
  <div class="stat" style="left:188px;top:708px;width:95px"><b>5,000+</b><span>Ecommerce business</span><br>partner with Brindle</div>
  <div class="stat" style="left:68px;top:794px;width:85px"><b>99.96%</b><span>of order ship on time</span><br>within SLA</div>
  <div class="stat" style="left:190px;top:794px;width:110px"><b><small style="font-size:11px">#</small>1</b><span>Best fulfillment Technology</span><br>by lorem ipsum dummy text</div>

  <svg class="abs" style="left:375px;top:591px" width="410" height="362"><ellipse cx="205" cy="181" rx="200" ry="176" fill="none" stroke="#aab" stroke-dasharray="3 3"/>
    <path d="M107 23 L150 60 M256 13 L230 60 M369 108 L312 115 M376 236 L312 240 M285 340 L300 270 M118 340 L200 270 M28 217 L76 230 M28 115 L76 118" stroke="#aab" stroke-dasharray="3 3" fill="none"/></svg>
  <div class="svc" style="left:451px;top:670px">Warehouse<br>Management Software</div>
  <div class="svc" style="left:575px;top:670px">3-Tier<br>Shipping</div>
  <div class="svc" style="left:451px;top:723px">Temperature Controlled<br>Shipping</div>
  <div class="svc" style="left:575px;top:723px">International<br>Shipping</div>
  <div class="svc" style="left:451px;top:776px">State Compliance</div>
  <div class="svc" style="left:575px;top:776px">Custom<br>Branded Box</div>
  <div class="svc" style="left:451px;top:829px">Inventory<br>Management and report</div>
  <div class="svc" style="left:575px;top:829px">Pick &amp; Tack</div>
  <div class="svc-icon" style="left:451px;top:583px"><svg width="34" height="30"><rect x="2" y="12" width="15" height="15" fill="none" stroke="#8a9aa6"/><rect x="17" y="12" width="15" height="15" fill="none" stroke="#8a9aa6"/><rect x="10" y="2" width="14" height="10" fill="none" stroke="#8a9aa6"/></svg></div>
  <div class="svc-icon" style="left:600px;top:573px"><svg width="30" height="30"><g fill="none" stroke="#8a9aa6"><rect x="2" y="3" width="6" height="6"/><rect x="2" y="13" width="6" height="6"/><rect x="2" y="23" width="6" height="6"/><path d="M12 6h16M12 16h16M12 26h16"/></g></svg></div>
  <div class="svc-icon" style="left:713px;top:668px"><svg width="30" height="30"><g fill="none" stroke="#8a9aa6"><circle cx="15" cy="15" r="13"/><ellipse cx="15" cy="15" rx="6" ry="13"/><path d="M2 15h26"/></g></svg></div>
  <div class="svc-icon" style="left:720px;top:796px"><svg width="30" height="30"><g fill="none" stroke="#8a9aa6"><rect x="3" y="10" width="16" height="16"/><rect x="11" y="3" width="16" height="16"/></g></svg></div>
  <div class="svc-icon" style="left:629px;top:900px"><svg width="32" height="30"><g fill="none" stroke="#8a9aa6"><rect x="2" y="2" width="12" height="12"/><path d="M18 4h12M18 9h12M18 14h12"/><rect x="3" y="18" width="5" height="10"/><rect x="12" y="21" width="5" height="7"/><rect x="22" y="19" width="5" height="9"/></g></svg></div>
  <div class="svc-icon" style="left:462px;top:900px"><svg width="34" height="28"><g fill="none" stroke="#8a9aa6"><rect x="5" y="3" width="24" height="17"/><path d="M1 24h32"/></g></svg></div>
  <div class="svc-icon" style="left:372px;top:777px"><svg width="34" height="26"><g fill="none" stroke="#8a9aa6"><rect x="2" y="3" width="20" height="15"/><path d="M22 8h6l4 5v5H22z"/><circle cx="8" cy="21" r="3"/><circle cx="26" cy="21" r="3"/></g></svg></div>
  <div class="svc-icon" style="left:372px;top:675px"><svg width="34" height="24"><g fill="none" stroke="#8a9aa6"><path d="M2 8h10M2 13h10M2 18h10"/><rect x="16" y="4" width="16" height="16"/></g></svg></div>

  <!-- why -->
  <p class="abs eyebrow" style="left:68px;top:1074px">Why Brindle?</p>
  <h2 class="abs heading why-title">Brindle freight is an end-to-end fulfillment provider trusted by thousand of LOREM brands</h2>
  <div class="abs barrels" role="img" aria-label="Photo of wine barrels stacked in a dark cellar"></div>
  <h3 class="abs heading" style="left:477px;top:1213px;font-size:22px;line-height:29px;width:260px">Powerful network of fulfillment centers</h3>
  <p class="abs para" style="left:477px;top:1280px;width:245px">We help you determine optimal inventory placement across our growing fulfillment network to improve delivery speeds and reduce shipping costs. You can scale efficiently by distributing inventory into additional warehouse over time.</p>
  <ul class="abs ticks" style="left:477px;top:1372px">
    <li>Affordable 2-day shipping</li>
    <li>Easy-to-understanding pricing</li>
    <li>Wide range of fulfillment services</li>
    <li>Transparency of performance for accountability</li>
    <li>Hands-off fulfillment so you can focus on everything else</li>
  </ul>
  <div class="abs" style="left:477px;top:1482px;display:flex;gap:26px;align-items:center">
    <span style="width:14px;height:16px;background:#555;border-radius:3px"></span>
    <span style="width:26px;height:8px;background:#555"></span>
    <span style="width:40px;height:6px;background:#777"></span>
    <span style="width:40px;height:8px;background:#999"></span>
  </div>
  <p class="abs" style="left:477px;top:1509px;font-size:8.5px;color:#333">We ship to anywhere in the world that the carriers deliver.</p>

  <!-- software band -->
  <section class="abs band">
    <div class="abs tabs"><div class="lead">All-In-One Cloud<br>Based Software Section</div><div class="on">Inventory</div><div>Order</div><div>Shipping</div><div>Warehouse</div></div>
    <h3 class="abs" style="left:68px;top:105px;font-size:13px;font-weight:600;color:#fff">Inventory Management</h3>
    <p class="abs" style="left:68px;top:128px;width:400px;font-size:9px;line-height:17px;color:#fff">With Brindle's inventory portal, you can kiss your cumbersome spreadsheets goodbye. Track inventory levels across multiple sales channels, identify your best selling SKUs, blacklist old SKUs, receive low stock alerts, and more. Brindle's inventory system will give you complete visibility and control of your inventory.</p>
    <div class="abs laptop" role="img" aria-label="Laptop showing an inventory report table" style="background:linear-gradient(180deg,#ffffff 0%,#ffffff 62%,#d9a98a 62%,#c9916f 100%);border:6px solid #d2a083;border-radius:8px 8px 4px 4px"></div>
  </section>

  <!-- warehouse -->
  <h2 class="abs wh-title">Warehouse <b>Location</b></h2>
  <p class="abs para" style="left:68px;top:1990px;width:305px">With Brindle's inventory portal, you can kiss your cumbersome spreadsheets goodbye. Track inventory levels across multiple sales channels, identify your best selling SKUs, blacklist old SKUs, receive low stock alerts, and more. Brindle's inventory system will give you complete visibility and control of your inventory.</p>
  <ul class="abs ticks" style="left:68px;top:2088px;font-size:8px">
    <li style="height:17px">Gain Competitive advantage</li>
    <li style="height:17px">Avoid Heat hold storage and losing customers</li>
    <li style="height:17px">Trucks leave every 2 weeks for inventory replacement</li>
    <li style="height:17px">Refrigerated trucks for temperature control</li>
    <li style="height:17px">Online inventory system to order from inventory from both warehouses.</li>
    <li style="height:17px">Put inventory closer to your customers to faster fulfillment</li>
  </ul>
  <div class="btn btn-solid" style="left:68px;top:2223px;width:104px;height:28px">Let's Go</div>
  <div class="abs map" role="img" aria-label="Outline map of the United States with three warehouse pins in the west, south and northeast"></div>

  <!-- ship -->
  <section class="abs ship">
    <h2 class="abs heading" style="left:0;top:134px;width:614px;text-align:center;font-size:22px;color:#fff">We ship all over the world</h2>
    <p class="abs" style="left:60px;top:173px;width:494px;text-align:center;font-size:10px;line-height:21px;color:#fff">We use our network of fulfillment centers to help you strategically split and manage your inventory to reduce shipping costs and transit times.</p>
    <div class="btn" style="left:232px;top:233px;width:150px;height:28px;background:#fff;color:var(--navy)">Talk to a Fulfillment Expert</div>
  </section>
  <div class="abs truck" role="img" aria-label="Front view of a white delivery truck with the Brindle Freight name on the cab"></div>

  <!-- testimonial -->
  <section class="abs testi">
    <div class="abs testi-left"></div>
    <div class="abs client">Halvern<br>Estate</div>
    <p class="abs" style="left:473px;top:82px;font-size:7.5px;color:var(--navy);font-weight:600">FEATURED CLIENT</p>
    <p class="abs quote">"We have been using BFL for some time. We got results via phone, email, everyone is always very courteous. The driver Dale is performing his job with pride and promptness. We have had only few claims and they have always been handled to our satisfaction."</p>
    <p class="abs" style="left:473px;top:300px;font-size:7.5px;line-height:9px;color:#333"><b>Marla Quist</b><br>Founder of Halvern Winery</p>
    <div class="arrow-btn" style="left:661px;top:296px"></div>
    <div class="arrow-btn" style="left:699px;top:296px"></div>
    <svg class="abs" style="left:661px;top:296px" width="62" height="24"><path d="M14 7 L9 12 L14 17" fill="none" stroke="#99a"/><path d="M48 7 L53 12 L48 17" fill="none" stroke="#99a"/></svg>
    <div class="btn btn-solid" style="left:757px;top:296px;width:84px;height:25px;font-size:8px">Read the Story</div>
  </section>

  <!-- footer -->
  <footer class="abs footer">
    <div class="abs logo" style="left:95px;top:36px;font-size:10px"><span class="logo-mark" style="width:11px;height:11px"></span>BRINDLE FREIGHT</div>
    <p class="abs" style="left:95px;top:68px;width:250px;font-size:8px;line-height:10px">We use our network of fulfillment centers to help you strategically split and manage your inventory to reduce shipping costs and transit times.</p>
    <p class="abs" style="left:95px;top:114px;font-size:8px;line-height:10px">418 Orchard Loop,<br>Valecrest, CA 90417</p>
    <p class="abs" style="left:95px;top:138px;font-size:8px;line-height:15px">&#9742; (555) 014 2290<br>&#10148; support@brindlefreight.com</p>
    <div class="foot-links">Location<br>Home<br>About<br>Hours of Operation<br>Career</div>
    <div class="abs" style="left:589px;top:36px;width:1px;height:145px;background:#9aa5ae"></div>
    <p class="abs" style="left:612px;top:60px;font-size:8.5px;color:var(--navy)">We ship all over the world</p>
    <p class="abs" style="left:612px;top:80px;font-size:7.5px">We will deliver to you on your preferred time</p>
    <div class="btn btn-solid" style="left:612px;top:98px;width:100px;height:23px;font-size:8px">Schedule Pick up</div>
    <p class="abs" style="left:612px;top:131px;font-size:8px;color:var(--navy);text-decoration:underline">Map &amp; Direction</p>
  </footer>
  <div class="abs bottom">© 2021 Brindle Freight. All rights reserved.</div>
</div>
</body>
</html>
```